Prominent Trial Lawyer need a Brochure Design for his firm

Harold J. Brantley of The Brantley Law Firm has been successfully trying severe and complex for over 28 years. He holds the largest verdict in the history of South Georgia of $150,000,000.00 before the late Leonard P. Vasquez in the Okefen District of the Southern District of Georgia. He specializes in sever injuries, whether by auto accident, trucking accident or medical malpractice. He is also well know for his successful trial of business disputes and high net-worth Divorces.
Target Market(s)
Persons who need an aggressive, experienced trial lawyer especially for personal injury, but also for other civil and business matters, high end divorde
Industry/Entity Type
Medical
Contact Information for Business Card
Need to use coloring and logo uplaoded
Requirements
Must have
- 1) biography of principal, Harold J. Brantley
- 2) what we do
- 3) specific cases handled, with specific outcomes (will be supplied)

```html
<!DOCTYPE html>
<html lang="en">
<head>
<meta charset="utf-8">
<title>The Brantley Law Firm – Tri Fold Brochure</title>
<link href="https://fonts.googleapis.com/css2?family=Arimo:ital,wght@0,400;0,700;1,700&family=Cinzel:wght@400;600&family=Crimson+Text:ital,wght@0,400;0,600;1,400&display=swap" rel="stylesheet">
<style>
  :root {
    --stage: #6d6d6d;
    --red: #e32a27;
    --red-deep: #b8151a;
    --red-dark: #8d0f12;
    --paper: #ffffff;
    --paper-shade: #ececec;
    --ink: #1d1d1d;
    --ink-soft: #3a3a3a;
  }
  * { margin: 0; padding: 0; box-sizing: border-box; }
  html, body { width: 769px; height: 1200px; overflow: hidden; }
  body { background: var(--stage); position: relative; font-family: "Crimson Text", serif; }

  .sheet-label {
    position: absolute; color: #fff;
    font-family: "Arimo", sans-serif; font-weight: 700; font-size: 19px; letter-spacing: .3px;
  }
  .label-title { left: 48px; top: 16px; }
  .label-side1 { left: 468px; top: 18px; }
  .label-side2 { left: 476px; top: 608px; }

  .spread { position: absolute; left: 37px; width: 695px; overflow: hidden; }
  .spread-outside { top: 54px; height: 537px; }
  .spread-inside { top: 634px; height: 536px; background: var(--paper); }
  .panel { position: absolute; top: 0; height: 100%; }

  /* left panel */
  .panel-welcome {
    left: 0; width: 232px;
    background: linear-gradient(180deg, var(--red) 0%, var(--red) 88%, var(--red-deep) 100%);
    color: #fff;
  }
  .welcome-heading {
    position: absolute; top: 20px; left: 0; width: 232px; text-align: center;
    font-family: "Cinzel", serif; font-weight: 600; font-size: 20px;
  }
  .welcome-heading::before, .welcome-heading::after {
    content: ""; position: absolute; top: 12px; width: 52px; height: 3px;
    border-top: 1px solid #fff; border-bottom: 1px solid #fff;
  }
  .welcome-heading::before { left: 3px; }
  .welcome-heading::after { right: 3px; }
  .welcome-sub {
    position: absolute; top: 48px; width: 232px; text-align: center;
    font-family: "Cinzel", serif; font-size: 14.5px;
  }
  .welcome-body {
    position: absolute; top: 73px; left: 20px; width: 197px;
    font-style: italic; font-size: 11.6px; line-height: 14.8px; text-align: justify;
  }
  .practice-heading {
    position: absolute; top: 376px; left: 14px;
    font-family: "Cinzel", serif; font-size: 14.5px;
  }
  .practice-list { position: absolute; top: 403px; left: 51px; list-style: none; }
  .practice-list li {
    display: flex; align-items: center; gap: 7px;
    font-size: 15.5px; line-height: 22.4px;
  }
  .practice-list svg { width: 13px; height: 13px; }

  /* middle panel */
  .panel-cover {
    left: 232px; width: 232px;
    background: linear-gradient(90deg, var(--paper-shade) 0%, var(--paper) 30%, var(--paper) 80%, var(--paper-shade) 100%);
  }
  .firm-mark { position: absolute; left: 0; width: 232px; text-align: center; }
  .cover-mark { top: 210px; }
  .mark-dot {
    display: block; margin: 0 auto 12px; width: 34px; height: 34px;
    border-radius: 50%; background: var(--red);
  }
  .mark-name {
    font-family: "Cinzel", serif; font-weight: 400; color: var(--ink);
    font-size: 26px; line-height: 30px;
  }
  .mark-tag {
    font-family: "Arimo", sans-serif; font-size: 10.5px; color: var(--red); margin-top: 2px;
  }
  .contact-list {
    position: absolute; top: 476px; left: 28px; list-style: none;
    font-family: "Arimo", sans-serif; font-size: 11.2px; color: var(--red); line-height: 14.6px;
  }
  .contact-list li { display: flex; align-items: center; gap: 7px; }
  .contact-list svg { width: 9px; height: 9px; }

  /* right panel */
  .panel-back { left: 464px; width: 231px; background: var(--paper); }
  .back-shape { position: absolute; left: 0; top: 0; }
  .name-bar {
    position: absolute; top: 0; left: 26px; width: 205px; height: 19px;
    background: var(--red-dark); color: #fff; text-align: center;
    font-family: "Cinzel", serif; font-weight: 600; font-size: 14px; line-height: 20px;
    border-bottom: 1px solid #d66;
  }
  .portrait-main {
    position: absolute; top: 19px; left: 26px; width: 205px; height: 170px;
    background: radial-gradient(ellipse at 55% 45%, #5a5a5a 0%, #2a2a2a 45%, #1a0a0a 75%, rgba(120,10,12,0) 100%);
  }
  .tagline-vertical {
    position: absolute; left: 3px; top: 255px; transform-origin: 0 0; transform: rotate(-90deg);
    font-family: "Arimo", sans-serif; font-weight: 700; font-size: 11.3px; color: #fff; white-space: nowrap;
  }
  .divider-vertical { position: absolute; left: 25px; top: 19px; width: 1px; height: 302px; background: rgba(255,255,255,.7); }
  .quote {
    position: absolute; top: 223px; left: 30px; width: 196px; text-align: center;
    font-family: "Arimo", sans-serif; font-weight: 700; font-style: italic; color: #fff;
    font-size: 11.3px; line-height: 13.7px;
  }
  .quote-source {
    position: absolute; top: 300px; right: 6px;
    font-family: "Arimo", sans-serif; font-weight: 700; font-style: italic; color: #fff; font-size: 11px;
  }
  .back-mark { position: absolute; top: 410px; left: 14px; display: flex; align-items: center; gap: 10px; }
  .back-mark .mark-dot { margin: 0; width: 30px; height: 30px; }
  .back-mark .mark-name { font-size: 20px; line-height: 22px; text-align: center; }
  .back-mark .mark-tag { text-align: center; font-size: 9.5px; }

  /* inside spread */
  .office-photo {
    position: absolute; top: 0; left: 0; width: 695px; height: 280px;
    background: linear-gradient(180deg, #8e8e8e 0%, #6a6a6a 35%, #4d5b3c 70%, #7a3a30 90%, var(--red) 100%);
  }
  .fold { position: absolute; top: 280px; width: 14px; height: 256px; background: linear-gradient(90deg, rgba(0,0,0,0), rgba(0,0,0,.06), rgba(0,0,0,0)); }
  .fold-one { left: 225px; }
  .fold-two { left: 457px; }
  .portrait-profile {
    position: absolute; top: 332px; left: 42px; width: 120px; height: 127px;
    border: 3px solid var(--red); border-radius: 6px;
    background: linear-gradient(180deg, #c9b8a8 0%, #8a7a70 50%, #1f2a44 100%);
  }
  .profile-name {
    position: absolute; top: 456px; left: 12px; width: 180px; text-align: center;
    font-family: "Arimo", sans-serif; font-weight: 700; font-size: 11.5px; color: var(--ink);
  }
  .profile-role {
    position: absolute; top: 470px; left: 12px; width: 180px; text-align: center;
    font-family: "Arimo", sans-serif; font-size: 8.5px; color: var(--red);
  }
  .rule-black { position: absolute; left: 195px; top: 290px; width: 2px; height: 150px; background: var(--ink); }
  .rule-red { position: absolute; left: 201px; top: 379px; width: 2px; height: 146px; background: var(--red); }
  .bio {
    position: absolute; top: 336px; left: 236px; width: 452px; text-align: center;
    font-size: 14.6px; line-height: 17.8px; color: var(--ink-soft);
  }
</style>
</head>
<body>
  <div class="sheet-label label-title">TRI FOLD BROCHURE</div>
  <div class="sheet-label label-side1">SIDE: 1</div>
  <div class="sheet-label label-side2">SIDE: 2</div>

  <section class="spread spread-outside">
    <div class="panel panel-welcome">
      <h2 class="welcome-heading">WELCOME</h2>
      <p class="welcome-sub">The Brantley Law Firm</p>
      <p class="welcome-body">Founded in 1989, the firm practices in business and general civil litigation, personal injury, real estate transaction and litigation, criminal defense, and family law. We love the practice of law and how it can help to resolve your civil and family disputes, to right the wrongs done by others, to protect your constitutional rights if you happened to be accused of a crime, to seek fair monetary compensation if you are entitled to. We at The Brantley Law Firm can ensure that you are best represented in courts utilizing the most up-to-date laws, diligent preparation and insightful understanding of your matter.</p>
      <h3 class="practice-heading">AREAS OF PRACTICE</h3>
      <ul class="practice-list">
        <li><svg viewBox="0 0 14 14"><path d="M1 8l4 4 8-11" fill="none" stroke="#fff" stroke-width="1.6"/></svg>Business Law</li>
        <li><svg viewBox="0 0 14 14"><path d="M1 8l4 4 8-11" fill="none" stroke="#fff" stroke-width="1.6"/></svg>Civil Litigation</li>
        <li><svg viewBox="0 0 14 14"><path d="M1 8l4 4 8-11" fill="none" stroke="#fff" stroke-width="1.6"/></svg>Criminal Defense</li>
        <li><svg viewBox="0 0 14 14"><path d="M1 8l4 4 8-11" fill="none" stroke="#fff" stroke-width="1.6"/></svg>Family Law</li>
        <li><svg viewBox="0 0 14 14"><path d="M1 8l4 4 8-11" fill="none" stroke="#fff" stroke-width="1.6"/></svg>Personal Injury</li>
      </ul>
    </div>

    <div class="panel panel-cover">
      <div class="firm-mark cover-mark">
        <span class="mark-dot"></span>
        <div class="mark-name">The Brantley<br>Law Firm</div>
        <div class="mark-tag">TRIAL LAWYER</div>
      </div>
      <ul class="contact-list">
        <li><svg viewBox="0 0 10 10"><rect width="10" height="10" rx="1.5" fill="#e32a27"/><path d="M5 2a2 2 0 0 1 2 2c0 1.5-2 4-2 4S3 5.5 3 4a2 2 0 0 1 2-2z" fill="#fff"/></svg>220 Oakridge Lane, Hollis, GA 31999</li>
        <li><svg viewBox="0 0 10 10"><rect width="10" height="10" rx="1.5" fill="#e32a27"/><path d="M3 2h1.5l.6 1.8-.9.7a5 5 0 0 0 1.3 1.3l.7-.9 1.8.6V7a1 1 0 0 1-1 1A5 5 0 0 1 2 3a1 1 0 0 1 1-1z" fill="#fff"/></svg>912-555-0142</li>
        <li><svg viewBox="0 0 10 10"><rect width="10" height="10" rx="1.5" fill="#e32a27"/><rect x="2" y="3" width="6" height="4" fill="#fff"/><path d="M2 3l3 2.3L8 3" fill="none" stroke="#e32a27" stroke-width=".8"/></svg>hbrantley@hjblaw.com</li>
      </ul>
    </div>

    <div class="panel panel-back">
      <svg class="back-shape" width="231" height="537" viewBox="0 0 231 537">
        <defs>
          <linearGradient id="backRed" x1="0" y1="0" x2="0" y2="1">
            <stop offset="0" stop-color="#8d0f12"/>
            <stop offset=".45" stop-color="#c4181c"/>
            <stop offset="1" stop-color="#e32a27"/>
          </linearGradient>
        </defs>
        <path d="M0 0H231V391C190 360 120 330 60 326C35 325 15 328 0 332Z" fill="url(#backRed)"/>
        <rect x="0" y="0" width="25" height="326" fill="#e32a27"/>
      </svg>
      <div class="portrait-main" role="img" aria-label="Portrait photograph of Harold J. Brantley in a dinner jacket"></div>
      <div class="divider-vertical"></div>
      <div class="name-bar">HAROLD J. BRANTLEY</div>
      <div class="tagline-vertical">WE'RE ALWAYS HERE TO HELP.</div>
      <p class="quote">“Whether you are against Insurance Companies, Major National Companies or Goverments, we level he field and give you the edge.”</p>
      <p class="quote-source">- The Brantley Law Firm</p>
      <div class="back-mark">
        <span class="mark-dot"></span>
        <div>
          <div class="mark-name">The Brantley<br>Law Firm</div>
          <div class="mark-tag">TRIAL LAWYER</div>
        </div>
      </div>
    </div>
  </section>

  <section class="spread spread-inside">
    <div class="office-photo" role="img" aria-label="Photograph of the firm's office building entrance with a stone sign, shrubs and stairs"></div>
    <div class="fold fold-one"></div>
    <div class="fold fold-two"></div>
    <div class="rule-black"></div>
    <div class="rule-red"></div>
    <div class="portrait-profile" role="img" aria-label="Portrait photograph of Harold J. Brantley in a suit and red tie"></div>
    <p class="profile-name">Harold J. Brantley</p>
    <p class="profile-role">Lawyer</p>
    <p class="bio">Harold J. Brantley of The Brantley Law Firm has been successfully trying severe and complex for over 28 years. He holds the largest verdict in the history of South Georgia of $150,000,000.00 before the late Leonard P. Vasquez in the Okefen District of the Southern District of Georgia. He specializes in sever injuries, whether by auto accident, trucking accident or medical malpractice. He is also well know for his successful trial of business disputes and high net-worth Divorces.</p>
  </section>
</body>
</html>
```